Current Employment Opportunities Email Template

We would like to redesign our internal job listing email template we send out each month. The email service we use is MailChimp and would like the template to be easy to edit when updating job postings. I attached an example below.

Font styles to use
Sans Serif

Colors

Designer to choose colors to be used in the design.

```html
<!DOCTYPE html>
<html lang="en">
<head>
<meta charset="utf-8">
<title>Today's Talent Opportunities – Brightwell Group</title>
<link rel="stylesheet" href="https://fonts.googleapis.com/css2?family=Jost:wght@500;600&family=Roboto:wght@400;500;700&display=swap">
<style>
  :root {
    --ink: #222222;
    --muted: #9a9a9a;
    --dark: #2b2b2b;
    --button-dark: #333333;
    --pale: #f6f6f6;
    --topbar: #eef0f2;
    --accent-sky: #2ebdf6;
    --accent-navy: #3d5a8e;
    --accent-green: #00bf8a;
    --teal: #17a8a8;
    --social: #cfcfcf;
    --white: #ffffff;
  }
  * { box-sizing: border-box; margin: 0; padding: 0; }
  html, body { width: 1200px; height: 3032px; overflow: hidden; background: var(--white); }
  body { font-family: "Roboto", Arial, sans-serif; color: var(--ink); position: relative; }

  .preheader {
    height: 76px; background: var(--topbar);
    display: flex; align-items: center; justify-content: center;
    font-size: 21px; color: #444;
  }
  .preheader a { color: #444; text-decoration: underline; }

  .brand {
    height: 234px; display: flex; align-items: center; justify-content: center;
  }
  .brand-name {
    font-family: "Roboto", Arial, sans-serif; font-weight: 700;
    font-size: 66px; letter-spacing: 3px; color: #1d1d1d;
  }

  .hero { position: relative; height: 470px; background: var(--pale); }
  .hero-band { position: absolute; top: 0; left: 0; width: 1200px; height: 204px; }
  .hero-title {
    position: absolute; top: 18px; width: 100%; text-align: center;
    font-family: "Jost", Arial, sans-serif; font-weight: 500; font-size: 53px;
    line-height: 72px; color: var(--white); letter-spacing: 0.5px;
  }
  .hero-tagline {
    position: absolute; top: 90px; width: 100%; text-align: center;
    font-size: 26px; line-height: 32px; color: var(--accent-sky);
  }
  .hero-tagline strong { font-weight: 500; }
  .hero-intro {
    position: absolute; top: 229px; left: 196px; width: 808px; text-align: center;
    font-size: 21.5px; line-height: 45px; color: #333;
  }

  .section-heading {
    height: 102px; background: var(--dark); color: var(--white);
    display: flex; align-items: center; justify-content: center;
    font-family: "Jost", Arial, sans-serif; font-weight: 600; font-size: 54px; letter-spacing: 1.5px;
  }

  .openings { width: 898px; margin: 17px auto 0; }
  .city { display: flex; margin-bottom: 15px; }
  .city-label {
    position: relative; width: 295px; flex: none;
    display: flex; align-items: center; justify-content: center;
    color: var(--white); font-weight: 700; font-size: 44px; letter-spacing: 1px;
  }
  .city-label svg { position: absolute; right: -37px; top: 50%; transform: translateY(-50%); }
  .city--dallas { height: 624px; }
  .city--austin { height: 303px; }
  .city--denver { height: 624px; }
  .city--dallas .city-label { background: var(--accent-sky); }
  .city--austin .city-label { background: var(--accent-navy); }
  .city--denver .city-label { background: var(--accent-green); }
  .city-jobs { flex: 1; background: var(--pale); }
  .city--austin .city-jobs { background: var(--white); }

  .job { position: relative; height: 312px; padding: 28px 0 0 49px; }
  .city--austin .job { height: 303px; }
  .job-title { font-size: 23px; font-weight: 700; letter-spacing: 0.5px; color: var(--ink); }
  .job-area { font-size: 20px; margin-top: 6px; color: var(--muted); }
  .job-area b { color: var(--ink); font-weight: 700; }
  .job-summary { font-size: 21px; line-height: 25px; margin-top: 18px; width: 420px; color: #2a2a2a; }
  .job-button {
    position: absolute; left: 49px; top: 216px; width: 472px; height: 59px;
    background: var(--teal); color: var(--white); text-decoration: none;
    display: flex; align-items: center; justify-content: center;
    font-size: 21px; font-weight: 500; letter-spacing: 0.5px;
  }

  .more-button {
    display: flex; align-items: center; justify-content: center;
    width: 898px; height: 89px; margin: 5px auto 0;
    background: var(--button-dark); color: var(--white); text-decoration: none;
    font-size: 37px; letter-spacing: 0.5px; border: 2px solid #222;
  }

  .social { position: absolute; top: 2668px; left: 0; width: 1200px; }
  .social-item {
    position: absolute; width: 110px; margin-left: -55px; text-align: center;
    font-size: 21px; color: #333; text-decoration: none;
  }
  .social-dot { display: block; width: 62px; height: 62px; margin: 0 auto 18px; border-radius: 50%; background: var(--social); }

  .footer-rule { position: absolute; top: 2836px; left: 217px; width: 764px; border-top: 2px solid #bdbdbd; }
  .footer-text { position: absolute; top: 2880px; width: 100%; text-align: center; font-size: 20.5px; line-height: 44px; color: #333; }
  .footer-text a { color: var(--accent-sky); }
</style>
</head>
<body>
  <div class="preheader">Don’t see this email properly?&nbsp;<a href="#">View in web browser</a></div>

  <header class="brand">
    <div class="brand-name">BRIGHTWELL GROUP</div>
  </header>

  <section class="hero">
    <svg class="hero-band" viewBox="0 0 1200 204" aria-hidden="true">
      <polygon points="0,0 1200,0 1200,134 600,200 0,134" fill="#2b2b2b"/>
    </svg>
    <h1 class="hero-title">TODAY’S TALENT OPPORTUNITIES</h1>
    <p class="hero-tagline">want to be a part of the most <strong>EFFICIENT &amp; ELITE</strong> team in the industry</p>
    <p class="hero-intro">We’ve got a list of opportunities here at Brightwell that we’d love to for you to strive for! These openings allow you to utilize your strengths, walk alongside us as we grow exponentially farther tahn we could ever dream, and leverage your successses to climb your way up the ladder of professional frowth and leadership within our organization!</p>
  </section>

  <h2 class="section-heading">CURRENT OPPORTUNITIES</h2>

  <main class="openings">
    <section class="city city--dallas">
      <div class="city-label">DALLAS
        <svg width="38" height="48" viewBox="0 0 38 48" aria-hidden="true"><polygon points="0,0 38,24 0,48" fill="#2ebdf6"/></svg>
      </div>
      <div class="city-jobs">
        <article class="job">
          <h3 class="job-title">REGIONAL SALES MANAGER</h3>
          <p class="job-area"><b>Area:</b> Dallas, TX</p>
          <p class="job-summary">Rewarding, fulfilling, and gola oriented position...</p>
          <a class="job-button" href="#">LEARN MORE ABOUT THIS OPPORTUNITY</a>
        </article>
        <article class="job">
          <h3 class="job-title">LEAD RESTORATION TECHNICIAN</h3>
          <p class="job-area"><b>Area:</b> Dallas, TX</p>
          <p class="job-summary">Restoration technician in the Dallas/Ft. Worth area...</p>
          <a class="job-button" href="#">LEARN MORE ABOUT THIS OPPORTUNITY</a>
        </article>
      </div>
    </section>

    <section class="city city--austin">
      <div class="city-label">AUSTIN
        <svg width="38" height="48" viewBox="0 0 38 48" aria-hidden="true"><polygon points="0,0 38,24 0,48" fill="#3d5a8e"/></svg>
      </div>
      <div class="city-jobs">
        <article class="job">
          <h3 class="job-title">JANITORAL SALES / ACCOUNT MANAGER</h3>
          <p class="job-area"><b>Area:</b> Austin, TX</p>
          <p class="job-summary">Rewarding, fulfilling, and gola oriented position...</p>
          <a class="job-button" href="#">LEARN MORE ABOUT THIS OPPORTUNITY</a>
        </article>
      </div>
    </section>

    <section class="city city--denver">
      <div class="city-label">DENVER
        <svg width="38" height="48" viewBox="0 0 38 48" aria-hidden="true"><polygon points="0,0 38,24 0,48" fill="#00bf8a"/></svg>
      </div>
      <div class="city-jobs">
        <article class="job">
          <h3 class="job-title">REGIONAL SALES MANAGER</h3>
          <p class="job-area"><b>Area:</b> Denver, CO</p>
          <p class="job-summary">Rewarding, fulfilling, and gola oriented position...</p>
          <a class="job-button" href="#">LEARN MORE ABOUT THIS OPPORTUNITY</a>
        </article>
        <article class="job">
          <h3 class="job-title">LEAD RESTORATION TECHNICIAN</h3>
          <p class="job-area"><b>Area:</b> Denver, CO</p>
          <p class="job-summary">Restoration technician in the Dallas/Ft. Worth area...</p>
          <a class="job-button" href="#">LEARN MORE ABOUT THIS OPPORTUNITY</a>
        </article>
      </div>
    </section>
  </main>

  <a class="more-button" href="#">CLICK HERE TO SEE MORE OPPORTUNITIES</a>

  <nav class="social" aria-label="Social links">
    <a class="social-item" href="#" style="left:398px"><span class="social-dot"></span>Circle</a>
    <a class="social-item" href="#" style="left:505px"><span class="social-dot"></span>Chirp</a>
    <a class="social-item" href="#" style="left:600px"><span class="social-dot"></span>Lens</a>
    <a class="social-item" href="#" style="left:695px"><span class="social-dot"></span>Scroll</a>
    <a class="social-item" href="#" style="left:790px"><span class="social-dot"></span>Website</a>
  </nav>

  <div class="footer-rule"></div>
  <footer class="footer-text">
    <p>©2018-2020 Brightwell Group. All rights reserved</p>
    <p>If you believe this has been sent to you in error, please safely <a href="#">unsubscribe.</a></p>
  </footer>
</body>
</html>
```